NEED A BUSINESS CARD FOR A NEW ELECTRICAL BUSINESS

HI I am after a new business card for my new electrical business I have a logo that I have attached its the one in blue, I would like that on the front and on the back my name- Marcus fell, Email marcusfell@tralvinet.com, mobile 0491570156, licence no# vic 48107, nsw 315042k I wont something that is a stand out from the rest but at the same time is neat as being a new business I wont it to catch peoples eye on the front of the card I would like the logo and not much else.
And on the back as well I would like a slogan saying something like
Quality-Reliable-Service

Hi all on the back of the card I would like a little slogan like Quality-Reliable-Service something like that would be good thanks

Hi all the business card needs to have both these licence numbers on it                                                  VIC-48107 nsw-315042k

```html
<!DOCTYPE html>
<html lang="en">
<head>
<meta charset="utf-8">
<title>Marcus Fell Electrical – Business Card</title>
<link rel="stylesheet" href="https://fonts.googleapis.com/css2?family=Open+Sans:wght@400;700&display=swap">
<style>
  :root {
    --stage: #2a2a2a;
    --card: #ffffff;
    --brand-blue: #1468b8;
    --icon-blue: #1a7fd0;
    --faint-blue: #e2ebf8;
    --band-blue: #e1eefa;
    --text-grey: #5a5a5a;
  }
  * { margin: 0; padding: 0; box-sizing: border-box; }
  html, body { width: 1200px; height: 472px; overflow: hidden; }
  body {
    position: relative;
    background: var(--stage);
    font-family: "Open Sans", Arial, sans-serif;
  }
  .card {
    position: absolute;
    top: 80px;
    width: 480px;
    height: 310px;
    background: var(--card);
  }
  .card--front { left: 80px; }
  .card--back  { left: 640px; }

  .brand {
    position: absolute;
    left: 0; right: 0;
    top: 132px;
    display: flex;
    align-items: center;
    justify-content: center;
    gap: 12px;
  }
  .brand__mark {
    width: 22px; height: 22px;
    background: var(--brand-blue);
  }
  .brand__name {
    font-weight: 700;
    font-size: 28px;
    letter-spacing: 1px;
    color: var(--brand-blue);
    text-transform: uppercase;
  }

  .watermark {
    position: absolute;
    left: 34px;
    top: 56px;
    font-weight: 700;
    font-size: 11px;
    letter-spacing: 0.5px;
    color: var(--faint-blue);
    text-transform: uppercase;
    white-space: nowrap;
  }
  .watermark-band {
    position: absolute;
    left: 196px;
    top: 65px;
    width: 250px;
    height: 9px;
    background: var(--band-blue);
  }

  .contacts {
    position: absolute;
    left: 274px;
    top: 137px;
    list-style: none;
  }
  .contacts li {
    display: flex;
    align-items: center;
    height: 32px;
    font-size: 11.5px;
    letter-spacing: 0.6px;
    color: var(--text-grey);
  }
  .contacts svg {
    width: 16px; height: 16px;
    margin-right: 8px;
    flex: none;
    fill: var(--icon-blue);
  }
  .contacts .no-icon { padding-left: 24px; }
</style>
</head>
<body>
  <section class="card card--front">
    <div class="brand">
      <span class="brand__mark"></span>
      <span class="brand__name">Marcus Fell Electrical</span>
    </div>
  </section>

  <section class="card card--back">
    <div class="watermark">Marcus Fell Electrical</div>
    <div class="watermark-band"></div>

    <ul class="contacts">
      <li>
        <svg viewBox="0 0 16 16" aria-hidden="true"><circle cx="8" cy="4.5" r="3.5"/><path d="M2 15c0-4 2.7-6 6-6s6 2 6 6z"/></svg>
        Marcus Fell
      </li>
      <li>
        <svg viewBox="0 0 16 16" aria-hidden="true"><path d="M4 1l2.5 3.5-1.6 1.6c.6 2 2.3 3.9 4.3 4.8l1.5-1.6L14.5 12 12.8 15C7 14.5 1.6 9 1.2 3z"/></svg>
        049 157 01 56
      </li>
      <li>
        <svg viewBox="0 0 16 16" aria-hidden="true"><path d="M1 3.5h14v9H1z M1.8 4.2L8 9l6.2-4.8" fill="none" stroke="#1a7fd0" stroke-width="1.4"/><path d="M1 3.5h14L8 9z"/></svg>
        marcusfell@tralvinet.com
      </li>
      <li>
        <svg viewBox="0 0 16 16" aria-hidden="true"><circle cx="8" cy="8" r="7.5"/><circle cx="8.6" cy="4.3" r="1.3" fill="#fff"/><path d="M6.4 6.8h3.2l-1.2 5.3h1.2v1H5.8v-1h1.1l.9-4.3H6.2z" fill="#fff"/></svg>
        Licence# vic 48107
      </li>
      <li class="no-icon">nsw 315042k</li>
    </ul>
  </section>
</body>
</html>
```